Tallwood Ridge firewood

It a new firewood outlet in Jindabyne nsw that will only sell top hardwood firewood (ironbark , red gum, grey gum, an box mix. I would like to see a web page the we can do order online payment for delivery. It will all so need to have photos of the firewood. I all so have logo for tallwood ridge firewood
Must have a modem look but easy to use I would like to see a black back ground of some sort.

Here are some other firewood web pages for ideas and firewood info
http://www.kestrelburnfuel.com.au
http://www.brindlefirewood.com.au
http://www.coppertonfirewood.com.au
http://www.wattleyhearthlogs.com.au/firewood

```html
<!DOCTYPE html>
<html lang="en">
<head>
<meta charset="utf-8">
<title>Tallwood Ridge Firewood</title>
<link rel="stylesheet" href="https://fonts.googleapis.com/css2?family=Roboto+Condensed:wght@400;700&family=Arimo:wght@400;700&display=swap">
<style>
:root{
  --blue:#1a6fba;
  --blue-light:#3d8fd6;
  --blue-dark:#155d9c;
  --page:#0f0f0f;
  --panel:#1a1a1a;
  --text:#f0f0f0;
  --muted:#a8a8a8;
  --dark-btn:#2c2c2c;
  --dark-btn-edge:#4a4a4a;
  --light-btn:#e6e6e6;
  --line:#333;
  --white:#fff;
}
*{margin:0;padding:0;box-sizing:border-box}
html,body{width:966px;height:1200px;overflow:hidden;background:var(--page)}
body{position:relative;font-family:"Arimo",Arial,sans-serif;color:var(--text)}
.abs{position:absolute}
.top-rule{left:0;top:0;width:966px;height:3px;background:#000}
.contact-strip{left:491px;top:3px;width:345px;height:30px;background:var(--panel);border-radius:0 0 4px 4px;font-size:9.5px;display:flex;align-items:center;justify-content:center;gap:14px;color:#ddd;white-space:nowrap}
.contact-strip b{color:var(--blue-light)}
.contact-strip a{color:var(--blue-light);text-decoration:underline}
.contact-strip svg{vertical-align:-2px;margin-right:6px}
.brand{left:130px;top:14px;width:160px;height:120px;display:flex;flex-direction:column;align-items:center;gap:10px}
.brand-dot{width:90px;height:90px;border-radius:50%;background:var(--blue)}
.brand-name{font-family:"Roboto Condensed",sans-serif;font-weight:700;font-size:15.5px;color:var(--blue-light);text-transform:uppercase;white-space:nowrap}
.search{left:390px;top:74px;width:190px;height:19px;border:1px solid #3a3a3a;background:#161616;display:flex}
.search span{flex:1;font-size:9.5px;color:#8a8a8a;padding:4px 7px}
.search i{width:20px;background:var(--blue);display:flex;align-items:center;justify-content:center}
.cart{left:626px;top:77px;font-size:10px;color:#ccc;white-space:nowrap}
.cart b{color:var(--blue-light);font-weight:400}
.cart svg{vertical-align:-2px;margin-right:6px}
.btn{display:inline-block;font-size:9px;font-weight:700;text-transform:uppercase;text-align:center;border-radius:3px;white-space:nowrap}
.btn-dark{background:var(--dark-btn);color:var(--white);border:1px solid var(--dark-btn-edge)}
.btn-light{background:var(--light-btn);color:#333;border:1px solid #ccc}
.order{left:752px;top:74px;width:84px;height:20px;line-height:18px}
.nav{left:0;top:146px;width:966px;height:26px;background:var(--blue)}
.nav ul{position:absolute;left:130px;top:0;display:flex;list-style:none;height:26px}
.nav li{font-size:9px;color:var(--white);text-transform:uppercase;display:flex;align-items:center;justify-content:center;border-right:1px solid var(--blue-dark)}
.nav li.active{background:#111}
.hero{left:0;top:172px;width:966px;height:354px;background:radial-gradient(ellipse 45% 55% at 50% 60%,#ffb020 0%,#f06a10 35%,#a8300a 62%,#5e2a18 85%,#3a1c12 100%)}
.hero-arrow{width:38px;height:38px;border-radius:50%;background:rgba(220,220,220,.75);top:331px;display:flex;align-items:center;justify-content:center}
.caption{left:343px;top:328px;width:281px;height:31px;background:var(--white);font-family:"Arimo",Arial,sans-serif;font-size:18px;text-align:center;line-height:31px;color:#222;white-space:nowrap}
.caption em{font-style:normal;color:var(--blue)}
.caption::after{content:"";position:absolute;left:134px;bottom:-7px;border:7px solid transparent;border-bottom:0;border-top-color:var(--white)}
.band{left:0;top:740px;width:966px;height:54px;background:linear-gradient(var(--page),#1d1d1d)}
.product{width:150px;top:551px;text-align:center}
.product .photo{width:122px;height:122px;border-radius:50%;margin:0 auto;border:3px solid #555;box-shadow:0 4px 8px rgba(0,0,0,.6)}
.product .photo.on{border-color:var(--blue)}
.product h3{font-family:"Roboto Condensed",sans-serif;font-weight:400;font-size:12.5px;margin-top:16px;color:var(--text)}
.product p{font-size:9.5px;margin-top:3px;color:#ccc}
.product p b{font-size:13px;color:var(--blue-light)}
.product .btn{width:56px;height:21px;line-height:19px;margin-top:10px}
.view-all{left:409px;top:778px;width:148px;height:27px;line-height:27px;background:var(--blue);color:var(--white);font-size:11px;text-align:center;border-radius:3px;text-transform:uppercase;white-space:nowrap}
.col{top:838px}
.col h2{font-family:"Roboto Condensed",sans-serif;font-weight:400;font-size:19px;color:var(--blue-light);text-transform:uppercase;white-space:nowrap}
.col p{font-size:9.3px;line-height:11px;color:var(--muted)}
.col .list{margin-top:17px;list-style:none}
.col .list li{display:flex;gap:10px;font-size:9.3px;line-height:11px;color:var(--muted);margin-bottom:13px}
.num{font-family:"Roboto Condensed",sans-serif;font-weight:700;font-size:17px;color:var(--text);width:20px;line-height:18px;flex:none}
.col .btn{position:absolute;height:19px;line-height:17px;left:0;top:154px}
.vrule{width:1px;top:838px;height:172px;background:var(--line)}
.footer{left:0;top:1050px;width:966px;height:150px;background:var(--blue);color:var(--white)}
.fcol{top:20px}
.fcol h4{font-size:9px;font-weight:700;text-transform:uppercase;margin-bottom:9px;white-space:nowrap}
.fcol ul{list-style:none}
.fcol li{font-size:8.5px;line-height:12.8px;white-space:nowrap}
.fcol li::before{content:"»  ";}
.frule{top:20px;width:1px;height:105px;background:rgba(255,255,255,.25)}
.cards,.socials{display:flex;gap:9px}
.card{width:30px;height:19px;background:var(--white);border-radius:2px}
.social{width:21px;height:21px;background:rgba(255,255,255,.3)}
.happy h4.happy-title{font-size:13.5px;text-transform:none;margin-bottom:9px}
.happy p{font-size:9px;line-height:11px}
.happy .btn{margin-top:13px;width:70px;height:19px;line-height:18px;background:#f2f2f2;color:#222}
</style>
</head>
<body>
<div class="abs top-rule"></div>

<div class="abs contact-strip">
  <span><svg width="10" height="9" viewBox="0 0 10 9"><path d="M1 3c0-2 8-2 8 0v1H7V3H3v1H1zM2 5h6l1 4H1z" fill="#ccc"/></svg>CALL US - <b>0400 555 018</b></span>
  <span><svg width="11" height="8" viewBox="0 0 11 8"><rect x=".5" y=".5" width="10" height="7" fill="none" stroke="#ccc"/><path d="M.5.5l5 4 5-4" fill="none" stroke="#ccc"/></svg>MAIL US - <a>info@tallwoodridgefirewood.com</a></span>
</div>

<div class="abs brand">
  <div class="brand-dot"></div>
  <div class="brand-name">Tallwood Ridge Firewood</div>
</div>

<div class="abs search"><span>Find Firewood Products ..</span><i><svg width="10" height="10" viewBox="0 0 10 10"><circle cx="4" cy="4" r="3" fill="none" stroke="#fff" stroke-width="1.6"/><path d="M6 6l3 3" stroke="#fff" stroke-width="1.8"/></svg></i></div>
<div class="abs cart"><svg width="12" height="10" viewBox="0 0 12 10"><path d="M0 1h2l2 6h6l1-4H3" fill="none" stroke="#ccc"/><circle cx="5" cy="9" r="1" fill="#ccc"/><circle cx="9" cy="9" r="1" fill="#ccc"/></svg>My Cart - <b>0</b> Item (s)</div>
<div class="abs btn btn-dark order">Order Online</div>

<nav class="abs nav"><ul>
  <li class="active" style="width:56px">Home</li>
  <li style="width:74px">About Us</li>
  <li style="width:78px">Products</li>
  <li style="width:93px">Accessories</li>
  <li style="width:70px">Delivery</li>
  <li style="width:56px">Faq`s</li>
  <li style="width:84px">Contact Us</li>
</ul></nav>

<div class="abs hero" role="img" aria-label="Photo of a hardwood fire burning inside a brick oven"></div>
<div class="abs hero-arrow" style="left:45px"><svg width="10" height="20" viewBox="0 0 10 20"><path d="M8 1L2 10l6 9" fill="none" stroke="#333" stroke-width="1.4"/></svg></div>
<div class="abs hero-arrow" style="left:883px"><svg width="10" height="20" viewBox="0 0 10 20"><path d="M2 1l6 9-6 9" fill="none" stroke="#333" stroke-width="1.4"/></svg></div>
<div class="abs caption"><em>TOP</em> HARDWOOD <em>FIREWOOD</em></div>

<div class="abs band"></div>

<div class="abs product" style="left:116px">
  <div class="photo on" role="img" aria-label="Close-up photo of split ironbark firewood" style="background:radial-gradient(#b06a3a,#4a2410)"></div>
  <h3>IRONBARK</h3><p>ONLY &nbsp;- &nbsp;<b>$12.30</b></p><span class="btn btn-dark">More</span>
</div>
<div class="abs product" style="left:311px">
  <div class="photo" role="img" aria-label="Photo of a pile of red gum firewood" style="background:radial-gradient(#c07a60,#6a3a2a)"></div>
  <h3>RED GUM</h3><p>ONLY &nbsp;- &nbsp;<b>$15.30</b></p><span class="btn btn-light">More</span>
</div>
<div class="abs product" style="left:504px">
  <div class="photo" role="img" aria-label="Photo of a stack of grey gum logs" style="background:radial-gradient(#9a9ea4,#4c5056)"></div>
  <h3>GREY GUM</h3><p>ONLY &nbsp;- &nbsp;<b>$12.30</b></p><span class="btn btn-light">More</span>
</div>
<div class="abs product" style="left:699px">
  <div class="photo" role="img" aria-label="Photo of a box mix fire burning in a fireplace" style="background:radial-gradient(#f0a030 0%,#8a3a10 35%,#1e1410 70%)"></div>
  <h3>BOX MIX</h3><p>ONLY &nbsp;- &nbsp;<b>$12.30</b></p><span class="btn btn-light">More</span>
</div>

<div class="abs view-all">View All Our Products</div>

<section class="abs col" style="left:130px;width:180px;height:172px">
  <h2>Welcome to our site</h2>
  <p style="margin-top:15px">Lorem ipsum dolor sit amet, consectetur adipisicing elit, sed do eiusmod tempor incididunt ut labore et dolore magna aliqua. Ut enim ad minim veniam, quis nostrud exercitation ullamco.</p>
  <p style="margin-top:11px">Duis aute irure dolor in reprehenderit in voluptate velit esse cillum dolore eu fugiat nulla pariatur ...</p>
  <span class="btn btn-dark" style="width:70px">Read More</span>
</section>
<div class="abs vrule" style="left:352px"></div>
<section class="abs col" style="left:390px;width:200px;height:172px">
  <h2>Why choose us?</h2>
  <ul class="list">
    <li><svg width="10" height="9" viewBox="0 0 10 9" style="flex:none;margin-top:1px"><path d="M1 5l3 3 5-7" fill="none" stroke="#888" stroke-width="2"/></svg>Lorem ipsum dolor sit amet, consectetur adipisicing elit.</li>
    <li><svg width="10" height="9" viewBox="0 0 10 9" style="flex:none;margin-top:1px"><path d="M1 5l3 3 5-7" fill="none" stroke="#888" stroke-width="2"/></svg>Lorem ipsum dolor sit amet, consectetur adipisicing elit.</li>
    <li><svg width="10" height="9" viewBox="0 0 10 9" style="flex:none;margin-top:1px"><path d="M1 5l3 3 5-7" fill="none" stroke="#888" stroke-width="2"/></svg>Lorem ipsum dolor sit amet, consectetur adipisicing elit.</li>
  </ul>
  <span class="btn btn-dark" style="width:70px">Read More</span>
</section>
<div class="abs vrule" style="left:610px"></div>
<section class="abs col" style="left:642px;width:200px;height:172px">
  <h2>Latest News</h2>
  <ul class="list">
    <li><span class="num">01</span>Lorem ipsum dolor sit amet, consectetur adipisicing elit.</li>
    <li><span class="num">02</span>Lorem ipsum dolor sit amet, consectetur adipisicing elit.</li>
    <li><span class="num">03</span>Lorem ipsum dolor sit amet, consectetur adipisicing elit.</li>
  </ul>
  <span class="btn btn-dark" style="width:60px">View All</span>
</section>

<footer class="abs footer">
  <div class="abs fcol" style="left:130px">
    <h4>Navigation</h4>
    <ul><li>Home</li><li>About Us</li><li>Products</li><li>Accessories</li><li>Contact Us</li></ul>
  </div>
  <div class="abs frule" style="left:230px"></div>
  <div class="abs fcol" style="left:264px">
    <h4>Order Online</h4>
    <ul><li>Terms &amp; Conditions</li><li>Delivery</li><li>Faq`s</li></ul>
  </div>
  <div class="abs frule" style="left:385px"></div>
  <div class="abs fcol" style="left:428px">
    <h4>Payment Option</h4>
    <div class="cards"><span class="card"></span><span class="card"></span><span class="card"></span></div>
    <h4 style="margin-top:20px">Follow Us On</h4>
    <div class="socials" style="gap:5px"><span class="social"></span><span class="social"></span><span class="social"></span><span class="social"></span></div>
  </div>
  <div class="abs frule" style="left:570px"></div>
  <div class="abs fcol happy" style="left:608px;top:18px;width:230px">
    <h4 class="happy-title">Happy Client`s</h4>
    <p>Lorem ipsum dolor sit amet, consectetur adipisicing elit, sed do eiusmod tempor incididunt ut labore et dolore magna aliqua.</p>
    <p style="margin-top:11px"><b>Rowan.</b> 15/06/13</p>
    <span class="btn">Read More</span>
  </div>
</footer>
</body>
</html>
```